PelloranDesk Postcard Campaign

We need a postcard design for our company, PelloranDesk.com - we are a job board for mechanics and auto technicians. We are sending a postcard to 1000 auto shops and trucking companies across the US to try to get them to come to our website and purchase a job pack and post a job posting. We will be offering them a promotion of "Save $20 on your first job post. Enter 'SUMMER20' at checkout."

We would like to see designs that are consistent with our website theme. The final design should communicate:
- Access to a targeted and local audience of only auto and truck mechanics and technicians
- Search 50,000 resumes
- Money back guarantee

Target Market(s)

Auto mechanic shops, car dealerships looking for mechanics, truck fleet management looking for technicians

Industry/Entity Type

It Company

Font styles to use
Sans Serif

Colors
0392cd
ec1f27
1b1b1b
cbcbcb
ffffff
3277b5

Requirements
Must have
• See content/copy upload
• - Match website color scheme and look and feel
Should not have
• No photos that look like stock photos - preferably steer away from photos unless it looks great

```html
<!DOCTYPE html>
<html lang="en">
<head>
<meta charset="utf-8">
<title>PelloranDesk Postcard – Front</title>
<link rel="stylesheet" href="https://fonts.googleapis.com/css2?family=Roboto:wght@300;400&family=Roboto+Condensed:ital,wght@0,400;0,700;1,700&display=swap">
<style>
  :root {
    --blue-deep: #1d4f80;
    --blue-mid: #3277b5;
    --blue-light: #3a86c2;
    --red: #ec1f27;
    --red-deep: #a51d22;
    --gray-light: #e4e4e4;
    --gray-mid: #cbcbcb;
    --gray-dark: #9a9a9a;
    --white: #ffffff;
    --ink: #1b1b1b;
    --label: #7a7a7a;
  }
  * { box-sizing: border-box; margin: 0; padding: 0; }
  html, body { width: 1200px; height: 1000px; overflow: hidden; background: var(--white); }
  body { position: relative; font-family: "Roboto Condensed", "Arial Narrow", sans-serif; }

  .postcard {
    position: absolute; left: 48px; top: 44px; width: 1106px; height: 858px;
    overflow: hidden;
    box-shadow: 4px 6px 8px rgba(0,0,0,0.35);
    background: radial-gradient(ellipse 60% 45% at 55% 25%, var(--blue-light), var(--blue-deep) 85%);
  }
  .band-gray {
    position: absolute; left: 0; top: 326px; width: 100%; height: 392px;
    background: radial-gradient(ellipse 70% 60% at 50% 45%, var(--gray-light), var(--gray-dark) 95%);
  }
  .band-footer {
    position: absolute; left: 0; top: 718px; width: 100%; height: 140px;
    background: radial-gradient(ellipse 50% 80% at 50% 40%, var(--blue-mid), var(--blue-deep) 90%);
  }

  .headline-top {
    position: absolute; left: 55px; top: 52px;
    font-family: "Roboto", sans-serif; font-weight: 300;
    font-size: 92px; line-height: 1; color: var(--white); letter-spacing: 1px;
  }
  .headline-main {
    position: absolute; right: 68px; top: 152px;
    font-family: "Roboto Condensed", sans-serif; font-weight: 700;
    font-size: 116px; line-height: 1; color: var(--white); letter-spacing: 0;
  }

  .feature {
    position: absolute; top: 278px; width: 296px; height: 308px;
    background: radial-gradient(circle at 50% 50%, var(--red), var(--red-deep) 80%);
    box-shadow: 3px 5px 10px rgba(0,0,0,0.35);
    color: var(--white); text-align: center;
    font-size: 26px; font-weight: 400;
    display: flex; flex-direction: column; justify-content: center;
  }
  .feature strong { font-weight: 700; }
  .feature--post { left: 90px; line-height: 55px; }
  .feature--reach { left: 404px; line-height: 41px; padding-bottom: 4px; }
  .feature--search { left: 716px; line-height: 55px; padding-bottom: 50px; }

  .promise {
    position: absolute; left: 0; width: 100%; text-align: center;
    font-style: italic; font-weight: 700; font-size: 33px; color: var(--white);
    letter-spacing: 0.6px;
    text-shadow: 1px 1px 3px rgba(0,0,0,0.35);
  }
  .promise--since { top: 608px; }
  .promise--guarantee { top: 656px; }

  .footer-brand, .footer-phone {
    position: absolute; top: 750px; font-weight: 700; color: var(--white);
    line-height: 50px;
  }
  .footer-brand { left: 148px; font-size: 44px; }
  .footer-mark { position: absolute; left: 566px; top: 739px; }
  .footer-phone { left: 672px; font-size: 46px; letter-spacing: 1px; }

  .sheet-label {
    position: absolute; right: 48px; top: 930px;
    font-family: "Roboto", sans-serif; font-weight: 300; font-size: 30px; color: var(--label);
  }
</style>
</head>
<body>
  <section class="postcard">
    <div class="band-gray"></div>
    <div class="band-footer"></div>

    <h1 class="headline-top">FIND YOUR NEXT</h1>
    <h2 class="headline-main">MECHANIC TODAY</h2>

    <div class="feature feature--post">
      <p><strong>Post a job</strong> with<br>us and get access<br>to <strong>hundreds</strong> of<br>qualified <strong>technicians</strong><br>in your area</p>
    </div>
    <div class="feature feature--reach">
      <p>Includes <strong>distribution</strong><br>and <strong>promotion</strong> across<br>multiple <strong>job boards</strong>,<br>such as Torqbayly.com,<br>Wrenchlanex,<br>Gearvistoro.com</p>
    </div>
    <div class="feature feature--search">
      <p>Search <strong>50,000+</strong><br><strong>resumes</strong>, with<br>new <strong>candidates</strong><br>added daily</p>
    </div>

    <p class="promise promise--since">Connecting automotive employers with qualified technicians since 2006</p>
    <p class="promise promise--guarantee">100% satisfaction guaranteed, or your money back!</p>

    <p class="footer-brand">PELLORANDESK.COM</p>
    <svg class="footer-mark" width="74" height="74" viewBox="0 0 74 74" aria-hidden="true">
      <circle cx="37" cy="37" r="33" fill="#ffffff"/>
    </svg>
    <p class="footer-phone">800.555.0142</p>
  </section>

  <p class="sheet-label">FRONT POSTCARD</p>
</body>
</html>
```